Small IT consulting firm needs a new web site

Quillmark Solutions, LLC is a company based out of Arizona with national presence. We work on both national, multinational, and international projects. We are Brindlesoft Partners. Heavy experience and work with Orbitline Control Kit, Vantra, Deskhub 720 . We offer Architecture, Design, Development, and implementation services. We have a specialty in Deskhub 720 migrations and implementations. We also have a specialized practice in Program and Project Management. The design message should foster a feeling of partnership and experience. Attached is my logo.

```html
<!DOCTYPE html>
<html lang="en">
<head>
<meta charset="utf-8">
<title>Quillmark Solutions, LLC</title>
<link href="https://fonts.googleapis.com/css2?family=Cinzel:wght@400;600&family=Lato:wght@400;700&family=Raleway:wght@500;600;700;800&display=swap" rel="stylesheet">
<style>
:root{
  --red:#d71f2b;
  --red-dark:#b5151f;
  --ink:#2b2b2b;
  --text:#555;
  --muted:#777;
  --grey-bg:#efefef;
  --soft-bg:#f8f8f8;
  --line:#cfcfcf;
  --white:#fff;
}
*{margin:0;padding:0;box-sizing:border-box}
html,body{width:1200px;height:2258px;overflow:hidden}
body{position:relative;background:var(--white);font-family:'Lato',sans-serif;color:var(--text)}
.abs{position:absolute}

/* header */
.site-header{left:0;top:0;width:1200px;height:122px;background:linear-gradient(#fff,#f1f1f1)}
.brand{left:86px;top:24px}
.brand-name{font-family:'Raleway',sans-serif;font-weight:800;font-size:44px;line-height:42px;color:var(--red);letter-spacing:1px}
.brand-sub{font-family:'Raleway',sans-serif;font-weight:600;font-size:15px;color:#555;letter-spacing:.5px;line-height:17px;margin-top:2px}
.brand-tag{font-family:'Raleway',sans-serif;font-size:10px;color:#555;letter-spacing:.5px}
.contact-bar{right:86px;top:24px;display:flex;gap:36px;font-size:20px;color:#555;font-family:'Lato',sans-serif}
.contact-bar span{display:flex;align-items:center;gap:10px}
.main-nav{left:440px;top:76px;width:760px;height:46px;background:linear-gradient(#6a6a6a,#3c3c3c);display:flex;align-items:center;clip-path:polygon(0 0,100% 0,100% 100%,22px 100%)}
.main-nav a{font-family:'Raleway',sans-serif;font-weight:700;font-size:14px;letter-spacing:.5px;color:#eee;text-decoration:none;flex:1;text-align:center;border-left:1px solid #777}
.main-nav a:first-child{border:none;flex:0 0 110px}
.main-nav a.active span{background:var(--red);padding:5px 9px}

/* hero */
.hero{left:0;top:122px;width:1200px;height:516px;background:radial-gradient(circle at 440px 240px,#cfe3f2 0,#7d8a96 12%,#3b3f45 40%,#1e2024 80%)}
.hero-panel{left:738px;top:183px;width:384px;height:384px;border-radius:50%;background:rgba(255,255,255,.93);text-align:center;padding-top:96px}
.hero-panel h2{font-family:'Cinzel',serif;font-weight:600;font-size:27px;line-height:32px;color:#333}
.hero-panel p{font-size:17px;line-height:26px;color:#444;margin:10px 34px 0}
.btn{display:inline-block;background:var(--red);color:#fff;font-family:'Raleway',sans-serif;font-weight:700;text-decoration:none;border-bottom:3px solid var(--red-dark)}
.hero-panel .btn{margin-top:16px;font-size:17px;padding:10px 26px}
.dots{display:flex;gap:10px;justify-content:center;margin-top:16px}
.dots i{width:14px;height:14px;border-radius:50%;background:#222}
.dots i.on{background:#fff;border:2px solid #222}

/* headings */
.section-title{left:0;width:1200px;text-align:center;font-family:'Raleway',sans-serif;font-weight:700;font-size:28px;color:var(--ink);letter-spacing:.5px}
.section-title em{font-style:normal;color:var(--red)}
.divider{left:326px;width:548px;height:14px}

/* welcome */
.welcome-lead{left:0;top:756px;width:1200px;text-align:center;font-family:'Raleway',sans-serif;font-size:21px;color:#444}
.welcome-copy{left:86px;top:802px;width:1028px;text-align:center;font-size:14px;line-height:24px;color:#444}
.welcome-btn{left:535px;top:898px;font-size:15px;padding:7px 14px}

/* services */
.services{left:0;top:980px;width:1200px;height:425px;background:var(--grey-bg)}
.service-card{top:1168px;width:243px;height:208px;background:linear-gradient(160deg,#6f7378,#4a4d52);border:1px solid #ccc;text-align:center;color:#fff}
.service-card h3{font-family:'Raleway',sans-serif;font-weight:600;font-size:20px;margin-top:63px}
.service-card p{font-size:14px;line-height:19px;margin:10px 18px 0;color:#eee}
.service-card .plus{position:absolute;left:96px;bottom:0;width:50px;height:18px;background:var(--red);clip-path:polygon(50% 0,100% 100%,0 100%);color:#fff;font-size:14px;font-weight:700;line-height:22px}
.service-badge{top:1082px;width:140px;height:140px}

/* specialize */
.specialize{left:0;top:1405px;width:1200px;height:570px;background:var(--soft-bg)}
.spec-item{left:86px;width:564px;display:flex;gap:18px}
.spec-icon{flex:0 0 78px;height:78px;border-radius:50%;background:#fff;border:2px solid #e2e2e2;display:flex;align-items:center;justify-content:center}
.spec-item h4{font-family:'Raleway',sans-serif;font-weight:600;font-size:18px;color:#333;margin-top:8px}
.spec-item p{font-size:14px;line-height:20px;color:#555;margin-top:8px}
.spec-rule{left:86px;width:564px;height:1px;background:#e0e0e0}
.video{left:685px;top:1523px;width:430px;height:395px;background:linear-gradient(160deg,#bfe2ea,#6fa6b8 55%,#2f5f74);border:1px solid #9ab}
.video-bar{left:0;bottom:0;width:100%;height:36px;background:#1b1b1b}

/* clients */
.clients{left:0;top:1975px;width:1200px;height:110px;background:var(--grey-bg)}
.clients-title{left:86px;top:2004px;font-family:'Raleway',sans-serif;font-weight:600;font-size:30px;line-height:33px;color:#333}
.clients-title em{font-style:normal;color:var(--red)}
.client{top:2004px;height:66px;background:#fff;border:1px solid #ddd;display:flex;align-items:center;justify-content:center;gap:7px;font-family:'Raleway',sans-serif;font-weight:700;font-size:14px;line-height:16px;color:#444;text-align:center}
.client i{flex:0 0 10px;height:10px;background:var(--red)}
.arrow{top:2024px;font-size:26px;color:#bbb;font-family:'Lato',sans-serif}

/* footer */
.footer-wave{left:0;top:2060px;width:1200px;height:198px}
.footer-links{left:86px;top:2184px;display:flex;font-family:'Raleway',sans-serif;font-weight:600;font-size:13px;color:#fff}
.footer-links a{color:#fff;text-decoration:none;padding:0 24px;border-left:1px solid rgba(255,255,255,.5)}
.footer-links a:first-child{padding-left:8px;border:none}
.copyright{left:94px;top:2215px;font-size:13px;color:#fff}
.follow{left:957px;top:2170px;font-family:'Raleway',sans-serif;font-weight:600;font-size:14px;color:#fff}
.social{left:958px;top:2202px;display:flex;gap:5px}
.social i{width:24px;height:24px;border-radius:50%;background:#e6e6e6;opacity:.85}
</style>
</head>
<body>

<header class="abs site-header">
  <div class="abs brand">
    <div class="brand-name">QUILLMARK</div>
    <div class="brand-sub">SOLUTIONS, LLC</div>
    <div class="brand-tag">PARTNERS IN EXPERIENCE.</div>
  </div>
  <div class="abs contact-bar">
    <span><svg width="24" height="24" viewBox="0 0 24 24"><circle cx="12" cy="12" r="11" fill="none" stroke="#d71f2b" stroke-width="2"/><path d="M8 6l2 0 1 3-1.5 1a7 7 0 0 0 4 4l1-1.5 3 1v2c0 1-1 1.5-2 1.5A10 10 0 0 1 6.5 8c0-1 .5-2 1.5-2z" fill="#d71f2b"/></svg>480-555-0142</span>
    <span><svg width="24" height="18" viewBox="0 0 24 18"><rect x="1" y="1" width="22" height="16" rx="2" fill="#d71f2b"/><path d="M2 2l10 8 10-8" fill="none" stroke="#fff" stroke-width="2"/></svg>hello@quillmark.example</span>
  </div>
  <nav class="abs main-nav">
    <a class="active" href="#"><span>HOME</span></a>
    <a href="#">ABOUT</a>
    <a href="#">SERVICES</a>
    <a href="#">TESTIMONIALS</a>
    <a href="#">CONTACT</a>
  </nav>
</header>

<section class="abs hero" role="img" aria-label="Businessman holding a glowing light bulb above his open hand, surrounded by network and business icons"></section>
<div class="abs hero-panel">
  <h2>LOREM IPSUM DOL<br>SIT AMET ADIPISCING</h2>
  <p>Lorem ipsum dolor sit amet, consectetur eleifend eros lacus, sed convallis augue</p>
  <a class="btn" href="#">Learn More</a>
  <div class="dots"><i></i><i class="on"></i><i></i><i></i></div>
</div>

<h1 class="abs section-title" style="top:682px"><em>WELCOME TO</em> QUILLMARK SOLUTIONS LLC</h1>
<svg class="abs divider" style="top:718px" viewBox="0 0 548 14"><path d="M0 5H548M0 9H548" stroke="#bbb"/><rect x="267" y="2" width="10" height="10" transform="rotate(45 272 7)" fill="#fff" stroke="#999"/></svg>
<p class="abs welcome-lead">Duis autem vel eum iriure dolor in hendrerit in vulputate velit esse molestie consequat, velillum</p>
<p class="abs welcome-copy">Lorem ipsum dolor sit amet, consectetuer adipiscing elit, sed diam nonummy nibh euismod tincidunt ut laoreet dolore magna aliquam erat volutpat. Ut wisi enim minim veniam, quis nostrud exerci tation ullamcorper suscipit lobortis nisl ut aliquip ex ea commodo consequat. Dolore eu feugiat nulla facilisis at vero eros et accumsan et iusto odio dignissim qui blandit praesent luptatum zzril delenit augue duis dolore te feugait nulla facilisi.</p>
<a class="abs btn welcome-btn" href="#">LEARN MORE</a>

<section class="abs services"></section>
<h2 class="abs section-title" style="top:999px"><em>OUR</em> SERVICES</h2>
<svg class="abs divider" style="top:1038px" viewBox="0 0 548 14"><path d="M0 5H548M0 9H548" stroke="#bbb"/><rect x="267" y="2" width="10" height="10" transform="rotate(45 272 7)" fill="#fff" stroke="#999"/></svg>

<div class="abs service-card" style="left:87px" role="img" aria-label="Architecture service, background photo of blueprints"><h3>Architecture</h3><p>Ut wisi enim ad minim veniam, quis nostrud exerci lobortis nisl ut aliquip ex ea commodo.</p><span class="plus">+</span></div>
<div class="abs service-card" style="left:349px" role="img" aria-label="Design service, background photo of colour swatches"><h3>Design</h3><p>Ut wisi enim ad minim veniam, quis nostrud exerci lobortis nisl ut aliquip ex ea commodo.</p><span class="plus">+</span></div>
<div class="abs service-card" style="left:611px" role="img" aria-label="Development service, background photo of puzzle pieces"><h3>Development</h3><p>Ut wisi enim ad minim veniam, quis nostrud exerci lobortis nisl ut aliquip ex ea commodo.</p><span class="plus">+</span></div>
<div class="abs service-card" style="left:872px" role="img" aria-label="Implementation service, background photo of puzzle pieces"><h3>Implementation</h3><p>Ut wisi enim ad minim veniam, quis nostrud exerci lobortis nisl ut aliquip ex ea commodo.</p><span class="plus">+</span></div>

<svg class="abs service-badge" style="left:139px" viewBox="0 0 140 140"><rect x="22" y="22" width="96" height="96" transform="rotate(45 70 70)" fill="#d71f2b"/><circle cx="70" cy="70" r="34" fill="#fff"/><path d="M54 70l14-12 14 12v14H54z" fill="none" stroke="#444" stroke-width="3"/><rect x="64" y="74" width="8" height="10" fill="#444"/><path d="M78 86l12-20 4 3-12 20-5 1z" fill="#444"/></svg>
<svg class="abs service-badge" style="left:401px" viewBox="0 0 140 140"><rect x="22" y="22" width="96" height="96" transform="rotate(45 70 70)" fill="#d71f2b"/><circle cx="70" cy="70" r="34" fill="#fff"/><path d="M70 50a20 20 0 1 0 4 40c4 0 3-5 1-7s0-6 4-6h6a5 5 0 0 0 5-6c-2-12-10-21-20-21z" fill="#444"/><circle cx="62" cy="60" r="3" fill="#fff"/><circle cx="74" cy="58" r="3" fill="#fff"/><circle cx="58" cy="73" r="3" fill="#fff"/></svg>
<svg class="abs service-badge" style="left:663px" viewBox="0 0 140 140"><rect x="22" y="22" width="96" height="96" transform="rotate(45 70 70)" fill="#d71f2b"/><circle cx="70" cy="70" r="34" fill="#fff"/><rect x="50" y="54" width="40" height="28" rx="2" fill="none" stroke="#444" stroke-width="3"/><path d="M64 88h12M70 82v6" stroke="#444" stroke-width="3"/><path d="M63 63l-5 5 5 5M77 63l5 5-5 5M72 61l-4 14" fill="none" stroke="#444" stroke-width="2"/></svg>
<svg class="abs service-badge" style="left:924px" viewBox="0 0 140 140"><rect x="22" y="22" width="96" height="96" transform="rotate(45 70 70)" fill="#d71f2b"/><circle cx="70" cy="70" r="34" fill="#fff"/><circle cx="63" cy="64" r="10" fill="none" stroke="#444" stroke-width="6" stroke-dasharray="4 3"/><circle cx="63" cy="64" r="4" fill="#444"/><circle cx="80" cy="80" r="7" fill="none" stroke="#444" stroke-width="5" stroke-dasharray="3 2"/></svg>

<section class="abs specialize"></section>
<h2 class="abs section-title" style="top:1429px"><em>WE</em> SPECIALIZE IN</h2>
<svg class="abs divider" style="top:1468px" viewBox="0 0 548 14"><path d="M0 5H548M0 9H548" stroke="#bbb"/><rect x="267" y="2" width="10" height="10" transform="rotate(45 272 7)" fill="#fff" stroke="#999"/></svg>

<div class="abs spec-item" style="top:1522px"><div class="spec-icon"><span style="width:22px;height:22px;background:var(--red)"></span></div><div><h4>Deskhub 720</h4><p>Ut wisi enim minim veniam, quis nostrud exerci tation ullamcorper norl suscipit lobortis nisl ut aliquip ex ea commodo consequat.</p></div></div>
<div class="abs spec-rule" style="top:1618px"></div>
<div class="abs spec-item" style="top:1625px"><div class="spec-icon"><span style="width:22px;height:22px;background:var(--red)"></span></div><div><h4>Vantra</h4><p>Ut wisi enim minim veniam, quis nostrud exerci tation ullamcorper norl suscipit lobortis nisl ut aliquip ex ea commodo consequat.</p></div></div>
<div class="abs spec-rule" style="top:1721px"></div>
<div class="abs spec-item" style="top:1728px"><div class="spec-icon"><svg width="40" height="40" viewBox="0 0 40 40"><path d="M20 4l16 16-16 16" fill="none" stroke="#d71f2b" stroke-width="4"/><path d="M4 20h20M17 13l7 7-7 7" fill="none" stroke="#d71f2b" stroke-width="4"/></svg></div><div><h4>Program</h4><p>Ut wisi enim minim veniam, quis nostrud exerci tation ullamcorper norl suscipit lobortis nisl ut aliquip ex ea commodo consequat.</p></div></div>
<div class="abs spec-item" style="top:1850px"><div class="spec-icon"><svg width="40" height="40" viewBox="0 0 40 40"><rect x="8" y="6" width="22" height="7" fill="#d71f2b"/><rect x="14" y="17" width="18" height="7" fill="#d71f2b"/><rect x="6" y="28" width="16" height="7" fill="#d71f2b"/><path d="M12 13v4M22 24v4" stroke="#d71f2b" stroke-width="3"/></svg></div><div><h4>Project Management</h4><p>Ut wisi enim minim veniam, quis nostrud exerci tation ullamcorper norl suscipit lobortis nisl ut aliquip ex ea commodo consequat.</p></div></div>

<div class="abs video" role="img" aria-label="Video still of a hand touching a glowing circuit board interface">
  <svg class="abs" style="left:180px;top:155px" width="70" height="50" viewBox="0 0 70 50"><rect width="70" height="50" rx="12" fill="#2b2b2b" opacity=".85"/><path d="M28 14l16 11-16 11z" fill="#fff"/></svg>
  <div class="abs video-bar">
    <svg width="430" height="36" viewBox="0 0 430 36"><rect x="12" y="13" width="3" height="10" fill="#fff"/><rect x="18" y="13" width="3" height="10" fill="#fff"/><rect x="34" y="16" width="300" height="4" fill="#555"/><rect x="34" y="16" width="140" height="4" fill="#d71f2b"/><circle cx="174" cy="18" r="6" fill="#fff"/><rect x="335" y="12" width="10" height="12" fill="#888"/><rect x="362" y="14" width="55" height="8" rx="4" fill="#444"/><circle cx="390" cy="18" r="8" fill="#ddd"/></svg>
  </div>
</div>

<section class="abs clients"></section>
<h2 class="abs clients-title"><em>Our</em><br>Clients</h2>
<span class="abs arrow" style="left:243px">‹</span>
<div class="abs client" style="left:278px;width:148px"><i></i>Harlow Bank</div>
<div class="abs client" style="left:446px;width:163px"><i></i>Kestrel Controls</div>
<div class="abs client" style="left:629px;width:178px"><i></i>Meridian Financial</div>
<div class="abs client" style="left:824px;width:115px">Ashford<br>Automation</div>
<div class="abs client" style="left:957px;width:122px">Calloway</div>
<span class="abs arrow" style="left:1102px">›</span>

<svg class="abs footer-wave" viewBox="0 0 1200 198" preserveAspectRatio="none"><path d="M0 90C300 50 800 60 1200 0V198H0z" fill="#d71f2b"/><path d="M0 82C300 42 800 52 1200 -8" fill="none" stroke="#666" stroke-width="6"/><path d="M0 96C400 60 850 62 1200 18" fill="none" stroke="#fff" stroke-width="4" opacity=".9"/></svg>
<nav class="abs footer-links"><a href="#">Home</a><a href="#">About Us</a><a href="#">Services</a><a href="#">Contact Us</a></nav>
<p class="abs copyright">© 2015 Quillmark Solutions. All Rights Reserved</p>
<p class="abs follow">FOLLOW US ON</p>
<div class="abs social" aria-label="Social links"><i></i><i></i><i></i><i></i></div>

</body>
</html>
```